Korean Homemade food restaurant just like what your mom cooks at home

I need a black and white simple and modern design according to my logo.
My restaurant name is Nal Som (meaning of home cooking).
I need to have 늘찬(Nal Som) in Korean need to be included. Once again 늘찬.
I am not sure if I need to include my name and number and adress.
Updates

늘찬 Nal Som 478 Harwell Rd. Clarksville, TN 37118 Mark Yoon Owner Cell:931-608-2913 Store:931-617-3084

Target Market(s)

business owners, university students

Industry/Entity Type

Restaurant

Contact Information for Business Card

This is traditional Korean food restaurant that targets university students during lunch and Korean business travelers at dinner.

Font styles to use
Sans Serif

Requirements
Must have
• Must have my logo.

```html
<!DOCTYPE html>
<html lang="en">
<head>
<meta charset="utf-8">
<title>Nal Som Business Card</title>
<link rel="stylesheet" href="https://fonts.googleapis.com/css2?family=Questrial&family=Jura:wght@500;700&family=Nanum+Gothic:wght@400&display=swap">
<style>
  :root {
    --page: #e4e4e4;
    --card: #ffffff;
    --ink: #1c1c1c;
    --swoosh: #b9b9b9;
    --light-text: #f2f2f2;
  }
  html, body {
    margin: 0;
    padding: 0;
    width: 1200px;
    height: 771px;
    overflow: hidden;
    background: var(--page);
  }
  .canvas {
    position: relative;
    width: 1200px;
    height: 771px;
  }
  .card {
    position: absolute;
    top: 231px;
    width: 540px;
    height: 309px;
    background: var(--card);
    box-shadow: 0 3px 10px rgba(0,0,0,0.18);
    overflow: hidden;
  }
  .card--front { left: 45px; }
  .card--back { left: 615px; }

  .brand {
    display: flex;
    align-items: center;
    gap: 14px;
    font-family: "Questrial", "Nanum Gothic", sans-serif;
    font-weight: 400;
    color: var(--ink);
    white-space: nowrap;
  }
  .brand__mark {
    flex: none;
    background: var(--ink);
    border-radius: 50%;
  }
  .brand__text {
    display: flex;
    flex-direction: column;
    align-items: center;
    line-height: 1;
  }
  .brand__korean {
    margin-top: 0.3em;
    font-size: 0.4em;
    letter-spacing: 0.15em;
  }
  .card--front .brand {
    position: absolute;
    left: 50%;
    top: 50%;
    transform: translate(-50%, -50%);
    font-size: 64px;
  }
  .card--front .brand__mark { width: 30px; height: 30px; }

  .card--back .backdrop {
    position: absolute;
    inset: 0;
  }
  .card--back .brand {
    position: absolute;
    left: 335px;
    top: 118px;
    font-size: 40px;
    gap: 10px;
  }
  .card--back .brand__mark { width: 18px; height: 18px; }

  .contact {
    position: absolute;
    left: 26px;
    top: 24px;
    font-family: "Jura", sans-serif;
    color: var(--light-text);
  }
  .contact__name {
    margin: 0;
    font-size: 17px;
    font-weight: 700;
    letter-spacing: 1.5px;
    text-transform: uppercase;
  }
  .contact__title {
    margin: 2px 0 0;
    font-size: 12px;
    font-weight: 500;
  }
  .contact__address {
    margin: 20px 0 0;
    font-size: 12px;
    font-weight: 500;
    line-height: 1.45;
  }
  .contact__list {
    list-style: none;
    margin: 18px 0 0;
    padding: 0;
    font-size: 11.5px;
    font-weight: 500;
  }
  .contact__list li {
    display: flex;
    align-items: center;
    gap: 8px;
    height: 21px;
  }
  .contact__list svg {
    width: 12px;
    height: 12px;
    fill: var(--light-text);
    flex: none;
  }
</style>
</head>
<body>
<main class="canvas">

  <section class="card card--front" aria-label="Business card front">
    <div class="brand">
      <span class="brand__mark" aria-hidden="true"></span>
      <span class="brand__text">
        <span class="brand__name">Nal Som</span>
        <span class="brand__korean" lang="ko">늘찬</span>
      </span>
    </div>
  </section>

  <section class="card card--back" aria-label="Business card back">
    <svg class="backdrop" viewBox="0 0 540 309" width="540" height="309" aria-hidden="true">
      <path d="M0 0 H380 C330 80 255 190 248 309 H0 Z" fill="var(--swoosh)"/>
      <path d="M0 0 H362 C305 80 236 190 228 309 H0 Z" fill="var(--ink)"/>
    </svg>

    <div class="contact">
      <p class="contact__name">Owen Hale</p>
      <p class="contact__title">Managing Director</p>
      <p class="contact__address">214 9th floor Plaza<br>Elm Road KTN</p>
      <ul class="contact__list">
        <li>
          <svg viewBox="0 0 24 24" aria-hidden="true"><path d="M6.6 10.8a15 15 0 0 0 6.6 6.6l2.2-2.2c.3-.3.7-.4 1-.2 1.1.4 2.3.6 3.6.6.6 0 1 .4 1 1V20c0 .6-.4 1-1 1C10.6 21 3 13.4 3 4c0-.6.4-1 1-1h3.5c.6 0 1 .4 1 1 0 1.3.2 2.5.6 3.6.1.3 0 .7-.2 1z"/></svg>
          014 562 7390
        </li>
        <li>
          <svg viewBox="0 0 24 24" aria-hidden="true"><path d="M7 1h10a2 2 0 0 1 2 2v18a2 2 0 0 1-2 2H7a2 2 0 0 1-2-2V3a2 2 0 0 1 2-2zm0 3v14h10V4zm5 15.2a1.2 1.2 0 1 0 0 2.4 1.2 1.2 0 0 0 0-2.4z"/></svg>
          014 562 7390
        </li>
        <li>
          <svg viewBox="0 0 24 24" aria-hidden="true"><path d="M6 2h9l3 3v4h2a2 2 0 0 1 2 2v7h-4v4H6v-4H2v-7a2 2 0 0 1 2-2h2zm2 2v5h8V6h-2V4zm0 11v5h8v-5z"/></svg>
          014 562 7390
        </li>
        <li>
          <svg viewBox="0 0 24 24" aria-hidden="true"><path d="M2 5h20v14H2zm2 2v.5l8 5.5 8-5.5V7zm0 3v7h16v-7l-8 5.5z"/></svg>
          hello@mailbox.com
        </li>
        <li>
          <svg viewBox="0 0 24 24" aria-hidden="true"><path d="M12 2a10 10 0 1 0 0 20 10 10 0 0 0 0-20zm6.9 6h-3a15 15 0 0 0-1.3-3.9A8 8 0 0 1 18.9 8zM12 4c.8 1.2 1.5 2.5 1.9 4h-3.8c.4-1.5 1.100-2.8 1.9-4zM4.3 14a8 8 0 0 1 0-4h3.4a16 16 0 0 0 0 4zm.8 2h3a15 15 0 0 0 1.3 3.9A8 8 0 0 1 5.1 16zm3-8h-3a8 8 0 0 1 4.3-3.9A15 15 0 0 0 8.1 8zM12 20c-.8-1.2-1.5-2.5-1.9-4h3.8c-.4 1.5-1.1 2.8-1.9 4zm2.3-6H9.7a14 14 0 0 1 0-4h4.6a14 14 0 0 1 0 4zm.3 5.9a15 15 0 0 0 1.3-3.9h3a8 8 0 0 1-4.3 3.9zm1.7-5.9a16 16 0 0 0 0-4h3.4a8 8 0 0 1 0 4z"/></svg>
          www.sitenamehere.com
        </li>
      </ul>
    </div>

    <div class="brand">
      <span class="brand__mark" aria-hidden="true"></span>
      <span class="brand__text">
        <span class="brand__name">Nal Som</span>
        <span class="brand__korean" lang="ko">늘찬</span>
      </span>
    </div>
  </section>

</main>
</body>
</html>
```